Tidecrest NZ Brand, Revenue, Promotions & Events

I need an innovative business card that pops my brand. I like the colours against darker gradients and i'm not afraid to be bold.

I run my own Business, Brand, Event & Promotion company. I specialise in breathing life into businesses and adding atmosphere to promotions and events. I am concept based lady that likes to test the boundaries and create stand out campaigns that connect with the consumer.

I have 12 years business experience in a realm of interesting fields form 11 years in coordinating international music festivals & promotions, 6 years in radio with 8 radio awards including a NZ radio award for best sales team in NZ and was the national brand and sales manager for New Zealands 1st indoor entertainment mall. With 10 years of experience in advertising sales, I have an eye for creating revenue streams for businesses and thrive on implementing campaigns that compliment those streams.

I love sayings like "Do what you love, love what you do" and believe that you can achieve anything you want.

I have been fortunate in my career that my connections have carried me without needing to promote my business however it is important that I start to do so.

Target Market(s)

Decision makers 25 to 54

Contact Information for Business Card

Petra Ollingham
Director
p. 022 587 3091
e. petra@tidecrest.nz
www.tidecrest.nz

FB, IG and Linkedin logo

Font styles to use
Sans Serif

Colors

Designer to choose colors to be used in the design.

Requirements
Must have
• Petra Ollingham
• Director
• p. 022 587 3091
• e. petra@tidecrest.nz
• www.tidecrest.nz
• FB, IG and Linkedin logo
Nice to have
• I am looking for a business card with character, that leaves my presence with my customer and makes them remember my brand & optimistic personality when i walk out the door.

```html
<!DOCTYPE html>
<html lang="en">
<head>
<meta charset="utf-8">
<title>Tidecrest NZ – Business Card</title>
<link rel="stylesheet" href="https://fonts.googleapis.com/css2?family=Lato:wght@400;700;900&family=Montserrat:wght@400;500;600&display=swap">
<style>
  :root {
    --backdrop: #2b2b2b;
    --card-white: #ffffff;
    --brand-blue: #29a8df;
    --ink: #1c1c1c;
    --tagline-grey: #8f8f8f;
    --on-blue: #ffffff;
  }
  * { margin: 0; padding: 0; box-sizing: border-box; }
  html, body { width: 1200px; height: 900px; overflow: hidden; }
  body {
    background: var(--backdrop);
    font-family: "Lato", sans-serif;
    position: relative;
  }
  .card {
    position: absolute;
    left: 240px;
    width: 720px;
    height: 411px;
    overflow: hidden;
  }
  .card--front { top: 30px; background: var(--card-white); }
  .card--back { top: 462px; background: var(--brand-blue); }

  /* brand lockup */
  .brand { position: absolute; display: flex; flex-direction: column; }
  .brand__row { display: flex; align-items: center; gap: 12px; }
  .brand__dot { border-radius: 50%; flex: none; }
  .brand__name {
    font-family: "Montserrat", sans-serif;
    font-weight: 500;
    letter-spacing: 0.06em;
    text-transform: uppercase;
    line-height: 1;
    white-space: nowrap;
  }
  .brand__tagline {
    font-family: "Montserrat", sans-serif;
    font-weight: 400;
    text-transform: uppercase;
    letter-spacing: 0.02em;
    white-space: nowrap;
  }

  .card--front .brand { left: 38px; top: 42px; }
  .card--front .brand__dot { width: 30px; height: 30px; background: var(--brand-blue); }
  .card--front .brand__name { font-size: 44px; color: var(--brand-blue); }
  .card--front .brand__tagline { font-size: 14px; color: var(--tagline-grey); margin-top: 8px; }

  .card--back .brand { right: 40px; bottom: 40px; align-items: flex-end; }
  .card--back .brand__dot { width: 46px; height: 46px; background: var(--on-blue); }
  .card--back .brand__name { font-size: 66px; color: var(--on-blue); }
  .card--back .brand__tagline { font-size: 20px; color: var(--on-blue); margin-top: 12px; }

  /* contact block */
  .contact-accent {
    position: absolute;
    left: 0; top: 186px;
    width: 40px; height: 74px;
    background: linear-gradient(90deg, rgba(41,168,223,0.75), rgba(41,168,223,0.25));
  }
  .contact {
    position: absolute;
    left: 56px; top: 186px;
    list-style: none;
    color: var(--ink);
    font-size: 15px;
    letter-spacing: 0.09em;
    line-height: 1.5;
  }

  /* person */
  .person {
    position: absolute;
    right: 40px; top: 196px;
    text-align: right;
  }
  .person__name {
    font-weight: 900;
    font-size: 26px;
    letter-spacing: 0.03em;
    text-transform: uppercase;
    color: var(--brand-blue);
  }
  .person__role {
    font-size: 15px;
    letter-spacing: 0.12em;
    color: var(--ink);
    margin-top: 2px;
  }
  .person-tab {
    position: absolute;
    right: 0; top: 198px;
    width: 12px; height: 40px;
    background: var(--brand-blue);
    border-radius: 4px 0 0 4px;
  }

  /* social */
  .social {
    position: absolute;
    left: 50%; bottom: 26px;
    transform: translateX(-50%);
    display: flex; gap: 12px;
    list-style: none;
  }
  .social__item {
    width: 18px; height: 18px;
    border: 1.5px solid var(--brand-blue);
    border-radius: 50%;
  }
</style>
</head>
<body>
  <section class="card card--front" aria-label="Business card front">
    <div class="brand">
      <div class="brand__row">
        <span class="brand__dot"></span>
        <span class="brand__name">Tidecrest NZ</span>
      </div>
      <span class="brand__tagline">Identity | Growth | Launches &amp; Campaigns</span>
    </div>

    <div class="contact-accent" role="img" aria-label="Blue dotted accent pattern"></div>
    <ul class="contact">
      <li>022 587 3091</li>
      <li>petra@tidecrest.nz</li>
      <li>www.tidecrest.nz</li>
    </ul>

    <div class="person">
      <p class="person__name">Petra Ollingham</p>
      <p class="person__role">Director</p>
    </div>
    <span class="person-tab"></span>

    <ul class="social" aria-label="Social profiles">
      <li class="social__item" aria-label="Social profile one"></li>
      <li class="social__item" aria-label="Social profile two"></li>
      <li class="social__item" aria-label="Social profile three"></li>
    </ul>
  </section>

  <section class="card card--back" aria-label="Business card back">
    <div class="brand">
      <div class="brand__row">
        <span class="brand__dot"></span>
        <span class="brand__name">Tidecrest NZ</span>
      </div>
      <span class="brand__tagline">Identity | Growth | Launches &amp; Campaigns</span>
    </div>
  </section>
</body>
</html>
```